Lantern of Renewal needs a business card design

I need a business card design for my company to promote my new Christian non-fiction book, "Where The River Bends Home." I also want it to promote my web site, www.lanternofrenewalbks.com. The book is about empowering people to be transformed through a deeper relationship with God. I am picturing a design with a dove over water that matches the colors of my book cover, blue, white, yellow, and orange. Fire and light would also be possible elements of the design. I would like to be able to use the dove by itself as a logo for my business. This is my first book and I do not know if others will follow. The name of my publishing company is Silver Harvest Press, named after Gideon in the Bible story from the book of Judges. My book was independently published and was recently selected as a finalist for the 2015 Bright Horizon SMALLPRESS book award in the Christian non-fiction genre.

Target Market(s)

People who are hungry for more of God and who want to experience deep change in their lives.

Industry/Entity Type

Business

Contact Information for Business Card

Dana Whitcombe
Author
Where The River Bends Home
4287 Maple Orchard Lane
Austin, Texas 78651-2097
512-555-0143 512-555-0178
dana-whitcombe@examplemail.net
www.lanternofrenewalbks.com

Colors
0355a3
3377b5
85acd3
cedeed
fbee3e
ffc214

Requirements
Must have
• A dove with a blue background, peaceful and appealing
Nice to have
• Water and fire or light
Should not have
• Violence or fear-producing images

```html
<!DOCTYPE html>
<html lang="en">
<head>
<meta charset="utf-8">
<title>Where The River Bends Home – Business Card</title>
<link rel="stylesheet" href="https://fonts.googleapis.com/css2?family=Questrial&family=Jost:wght@500;700&family=Dancing+Script:wght@400;500&display=swap">
<style>
  :root {
    --page-bg: #e9e9ea;
    --sky-deep: #1d4f8e;
    --sky-mid: #3377b5;
    --sky-soft: #85acd3;
    --mist: #cedeed;
    --white: #ffffff;
    --gold: #ffc214;
    --band: rgba(38, 96, 165, 0.82);
    --navy-rule: #23538f;
    --ink: #16213a;
    --title-ink: #14233d;
    --script-ink: #eef3fa;
  }
  * { margin: 0; padding: 0; box-sizing: border-box; }
  html, body { width: 1200px; height: 750px; overflow: hidden; background: var(--page-bg); }

  .business-card {
    position: absolute;
    left: 100px; top: 89px;
    width: 1000px; height: 572px;
    overflow: hidden;
    background:
      radial-gradient(ellipse 520px 360px at 390px 10px, rgba(255,255,255,0.95), rgba(255,255,255,0) 70%),
      radial-gradient(ellipse 700px 260px at 200px 560px, rgba(255,255,255,1), rgba(255,255,255,0) 75%),
      linear-gradient(180deg, var(--sky-deep) 0%, var(--sky-mid) 30%, var(--sky-soft) 55%, var(--mist) 72%, var(--white) 90%);
    box-shadow: 0 2px 6px rgba(0,0,0,0.12);
  }

  .book-title {
    position: absolute; left: 39px; top: 48px;
    font-family: "Questrial", sans-serif;
    font-size: 48px; letter-spacing: 0.5px;
    color: var(--title-ink);
    white-space: nowrap;
  }
  .award-note {
    position: absolute; left: 39px; top: 104px;
    font-family: "Dancing Script", cursive;
    font-size: 18px;
    color: var(--title-ink);
    white-space: nowrap;
  }

  .name-band {
    position: absolute; left: 0; top: 202px;
    width: 583px; height: 105px;
    background: var(--band);
  }
  .author-name {
    position: absolute; left: 28px; top: 6px;
    font-family: "Jost", sans-serif; font-weight: 700;
    font-size: 58px; letter-spacing: 1px;
    color: var(--gold);
    white-space: nowrap;
  }
  .author-role {
    position: absolute; right: 42px; top: 58px;
    font-family: "Dancing Script", cursive; font-weight: 500;
    font-size: 36px; letter-spacing: 3px;
    color: var(--script-ink);
  }

  .dove-art {
    position: absolute; left: 630px; top: 181px;
    width: 307px; height: 268px;
  }

  .contact-list {
    position: absolute; left: 30px; top: 358px;
    list-style: none;
    font-family: "Jost", sans-serif; font-weight: 500;
    font-size: 21px; color: var(--ink);
  }
  .contact-item {
    position: relative;
    padding-left: 46px;
    line-height: 31px;
  }
  .contact-item.gap { margin-top: 6px; }
  .contact-icon {
    position: absolute; left: 6px; top: 7px;
    width: 18px; height: 18px;
  }

  .base-rule {
    position: absolute; left: 0; bottom: 0;
    width: 100%; height: 12px;
    background: var(--navy-rule);
  }
</style>
</head>
<body>
<main class="business-card">
  <h1 class="book-title">Where The River Bends Home</h1>
  <p class="award-note">finalist for the 2015 Bright Horizon SMALLPRESS book award in the Christian non-fiction genre</p>

  <div class="name-band">
    <h2 class="author-name">Dana Whitcombe</h2>
    <span class="author-role">author</span>
  </div>

  <svg class="dove-art" role="img" aria-label="White paper-folded dove in flight, the author's emblem" viewBox="0 0 307 268">
    <defs>
      <radialGradient id="doveGlow" cx="50%" cy="50%" r="50%">
        <stop offset="0%" stop-color="#ffffff" stop-opacity="0.9"/>
        <stop offset="100%" stop-color="#ffffff" stop-opacity="0"/>
      </radialGradient>
    </defs>
    <ellipse cx="153" cy="134" rx="150" ry="130" fill="url(#doveGlow)"/>
  </svg>

  <ul class="contact-list">
    <li class="contact-item">
      <svg class="contact-icon" viewBox="0 0 24 24"><path fill="var(--gold)" d="M6.6 10.8a15.1 15.1 0 0 0 6.6 6.6l2.2-2.2c.3-.3.7-.4 1-.2 1.1.4 2.3.6 3.6.6.6 0 1 .4 1 1V20c0 .6-.4 1-1 1A17 17 0 0 1 3 4c0-.6.4-1 1-1h3.5c.6 0 1 .4 1 1 0 1.3.2 2.5.6 3.6.1.3 0 .7-.2 1z"/></svg>
      78651-2097
    </li>
    <li class="contact-item">512-555-0143 | 512-555-0178</li>
    <li class="contact-item">
      <svg class="contact-icon" viewBox="0 0 24 24"><rect x="2" y="5" width="20" height="14" rx="1.5" fill="none" stroke="var(--gold)" stroke-width="2"/><path d="M3 6l9 7 9-7" fill="none" stroke="var(--gold)" stroke-width="2"/></svg>
      dana-whitcombe@examplemail.net
    </li>
    <li class="contact-item gap">
      <svg class="contact-icon" viewBox="0 0 24 24"><g fill="none" stroke="var(--gold)" stroke-width="1.8"><circle cx="12" cy="12" r="9.5"/><ellipse cx="12" cy="12" rx="4.2" ry="9.5"/><path d="M2.5 12h19M4 7h16M4 17h16"/></g></svg>
      www.lanternofrenewalbks.com
    </li>
    <li class="contact-item gap">
      <svg class="contact-icon" viewBox="0 0 24 24"><path fill="var(--gold)" d="M12 2a7 7 0 0 0-7 7c0 5.2 7 13 7 13s7-7.8 7-13a7 7 0 0 0-7-7zm0 9.5A2.5 2.5 0 1 1 12 6.5a2.5 2.5 0 0 1 0 5z"/></svg>
      4287 Maple Orchard Lane Austin, TX
    </li>
  </ul>

  <div class="base-rule"></div>
</main>
</body>
</html>
```